Coffee ecommerce website design

We are re-branding our website, starting with the logo which has now been done (see uploaded files).

Our website sells coffee and coffee-related products and accessories, with the vast majority of products not available in the supermarket or coffee shop - these brands are known, just not widely available in the UK. Our customers either know the product or brand because they have tried it somewhere (abroad), know of it (for example, if they are Italian) or they want to try something different.

The website has to be clean and simple (currently it is too cluttered) and make it easy to promote products. At the same time, not too simple that it looks cheap. Of course we don't claim to be anything like these, but to give you an idea, this is what we mean by clean, simple, professional ecommerce:
- http://www.marrowfield.com/home-garden/c500006
- http://www.pokertwine.com
- http://www.quillandthorpe.com
- http://www.vorlettishop.it
- http://www.52harbor.co.uk

Currently we are only looking for the design work - development can be discussed at a later date if you like.

Please take any assets such as images, text, etc. from our current website.

If you require any further information, please do ask. We would like to see the home page, category page and product page.

Many thanks,
Updates

Hi, we've seen some great designs so far - it will help to also see some product pages. Thanks.

Target Market(s)

Predominantly men and women between 35 and 60, descent income who enjoy good quality food and drink. The majority know their coffee, and are fussy about the coffee they drink.

Requirements
Must have
• Font - modern and maybe different, like Open Sans, Bree, Source Sans Pro.
• Strips/boxes where we can promote free delivery over £60, our loyalty points, quick turnaround, etc. Look at the top of our current website http://www.brewlantern.co.uk or underneath the menu bar of http://www.52harbor.co.uk (we like this simplicity and cleanliness by the way).
• Sorry if the following sounds obvious, but just to clarify, we would need the home page to have following (always following the route of cleanliness and simplicity...):
• - Menu//navigation bar
• - Search box
• - Telephone number
• - SSL seal (see side of current website)
• - Payment methods (we don't need all the card logos to be shown, just some sort of reference to CoinPass, Zerbix and Credit/Debit Cards)
• - Social media icons for Chatterly, chirpex, clipvault, Snapmoor, zerbix+ and Boardly
• - Selected products on the home page like we currently have under the HOT PRODUCTS section (see below, as we are looking to change this title to NEW ARRIVALS).
• - Coupon request by email box as per current site
• - Product rating icons (currently stars, but these can be unique/different)
• - Paragraph(s) of text for around 200 words
• - Cart value icon (have a look at http:.//www.velhaven.co.uk and see the red circle)
• - Carousel
• For the product page, the page must feature:
• - Product Title, quantity box, price, add to cart, availability, item reviews, product description (between 100 and 200 words, in paragraph and bullet points)
• - Product options (size, colour)
• - Social media share icons (Chatterly, chirpex and Boardly only)
• - Cross selling (Similar items)
• - Up-selling (buy these 2 items together and save xx%)
• - One this we will be adding is filtering by attribute, so for example, http://www.rkhollis.co.uk/All-Suits/Mens-Suit-Bundles,en_GB,sc.html where you can select colour, size, etc.
Nice to have
• If you can make it work, we'd like a NEW ARRIVALS/NEWEST PRODUCTS/JUST IN products area (on our current site we have HOT PRODUCTS for example).
• We want to promote the brands we sell by showing the logos, such as http://www.dawnroastery.co.uk (but not scrolling).
• Our strategy includes creating videos for some products, so somewhere on the product page we would like to have a ClipVault video embedded.

```html
<!DOCTYPE html>
<html lang="en">
<head>
<meta charset="utf-8">
<title>brewlantern.co.uk – Home</title>
<link rel="stylesheet" href="https://fonts.googleapis.com/css2?family=Open+Sans:ital,wght@0,400;0,600;0,700;1,400;1,600&display=swap">
<style>
:root{
  --red:#e2401c;
  --ink:#222;
  --text:#555;
  --muted:#8a8a8a;
  --nav:#3a3a3a;
  --nav-dark:#2b2b2b;
  --line:#e3e3e3;
  --tile:#c9c9c9;
  --page:#ffffff;
  --stage:#eef0f2;
}
*{box-sizing:border-box;margin:0;padding:0}
html,body{width:1200px;height:600px;overflow:hidden}
body{background:var(--stage);font-family:'Open Sans',Arial,sans-serif;color:var(--text);font-size:11px}
.page{width:1200px;height:600px;background:var(--page);overflow:hidden}
.wrap{width:1120px;margin:0 auto}

/* header */
.site-header{display:flex;justify-content:space-between;align-items:flex-start;height:66px;padding-top:14px}
.brand{display:flex;align-items:center;gap:8px;margin-top:6px}
.brand-dot{width:30px;height:30px;border-radius:50%;background:var(--red)}
.brand-name{font-size:24px;font-weight:700;color:var(--ink);letter-spacing:-.5px}
.header-tools{display:flex;flex-direction:column;align-items:flex-end;gap:8px}
.call-box{background:var(--nav-dark);color:#fff;font-size:9px;font-weight:600;padding:4px 8px}
.tools-row{display:flex;align-items:center;gap:14px}
.social{display:flex;gap:8px;font-size:8px;color:var(--muted)}
.search{width:150px;height:18px;border:1px solid var(--line);font-size:8px;color:var(--muted);padding:2px 6px}

/* nav */
.main-nav{display:flex;background:var(--nav);height:38px}
.main-nav a{width:98px;display:flex;align-items:center;justify-content:center;text-align:center;color:#fff;text-decoration:none;font-size:10px;font-weight:600;line-height:1.15;border-right:1px solid #4a4a4a}
.main-nav a.active{background:var(--red)}

/* hero */
.hero{position:relative;height:220px;background:radial-gradient(ellipse at 65% 45%,#7a5a3e 0%,#3b2818 38%,#140d08 75%);margin-top:0}
.hero-caption{position:absolute;left:0;bottom:0;right:0;background:rgba(0,0,0,.55);color:#eee;padding:8px 14px}
.hero-caption h2{font-size:14px;font-style:italic;font-weight:600;color:#fff}
.hero-caption p{font-size:8.5px;margin-top:2px}
.hero-arrows{position:absolute;right:12px;bottom:14px;display:flex;gap:3px}
.hero-arrows span{width:16px;height:16px;background:#111;display:flex;align-items:center;justify-content:center}

/* body */
.content{display:flex;gap:24px;margin-top:14px}
.sidebar{width:210px;flex:none}
.side-title{color:var(--red);font-size:12px;font-weight:600;margin:4px 0 3px}
.side-list{list-style:none}
.side-list li{font-size:8px;text-transform:uppercase;color:var(--text);padding:3px 0 3px 2px;border-bottom:1px solid #f0f0f0}
.more{text-align:right;font-size:8px;font-weight:700;color:var(--ink);margin:3px 0 6px}
.main{flex:1}
.welcome h1{font-size:15px;color:var(--red);font-weight:600}
.welcome h1 em{font-style:italic;font-weight:700}
.welcome h2{font-size:15px;color:var(--red);font-weight:400;margin-bottom:6px}
.welcome p{font-size:9px;line-height:1.5;margin-bottom:4px}
.read-more{display:block;width:max-content;margin:4px 0 0 auto;background:var(--red);color:#fff;font-size:9px;font-weight:600;padding:4px 10px}
.section-bar{display:flex;align-items:center;gap:8px;background:var(--nav-dark);color:#fff;font-weight:700;font-size:11px;height:26px;padding:0 10px;margin-top:12px}
.product-grid{display:grid;grid-template-columns:repeat(4,1fr);gap:14px;margin-top:12px}
.product-img{height:88px;background:linear-gradient(#d2d2d2,#bdbdbd)}
.product-name{font-size:8.5px;margin-top:4px;color:var(--ink)}
.product-price{font-size:8.5px;color:var(--muted)}
</style>
</head>
<body>
<div class="page">
  <div class="wrap">
    <header class="site-header">
      <div class="brand"><span class="brand-dot"></span><span class="brand-name">brewlantern.co.uk</span></div>
      <div class="header-tools">
        <div class="call-box">Got a question? Call us on 020 7946 0321</div>
        <div class="tools-row">
          <div class="social"><span>Chatterly</span><span>chirpex</span><span>clipvault</span><span>zerbix+</span></div>
          <div class="search">Search here...</div>
        </div>
      </div>
    </header>

    <nav class="main-nav">
      <a class="active">Home</a>
      <a>Coffee<br>Beans</a>
      <a>Ground<br>Coffee</a>
      <a>Coffee<br>Pods</a>
      <a>Coffee<br>Machines</a>
      <a>Moka<br>Pots</a>
      <a>Gift<br>Corner</a>
    </nav>

    <section class="hero" role="img" aria-label="Photo of a cup of espresso on a saucer surrounded by coffee beans on a dark background">
      <div class="hero-caption">
        <h2>Hello world</h2>
        <p>Lorem ipsum dolor sit amet, consectetur adipiscing elit, sed do eiusmod tempor incididunt ut labore et dolore magna aliqua. Ut enim ad minim veniam, quis nostrud exercitation.</p>
      </div>
      <div class="hero-arrows">
        <span><svg width="8" height="8" viewBox="0 0 8 8"><path d="M5.5 1 2.5 4l3 3" stroke="#fff" fill="none" stroke-width="1.4"/></svg></span>
        <span><svg width="8" height="8" viewBox="0 0 8 8"><path d="M2.5 1l3 3-3 3" stroke="#fff" fill="none" stroke-width="1.4"/></svg></span>
      </div>
    </section>

    <div class="content">
      <aside class="sidebar">
        <h3 class="side-title">Online Store</h3>
        <ul class="side-list">
          <li>Christmas Shop</li><li>New Items</li><li>Coffee Beans</li><li>Coffee Tins</li><li>Ground Coffee</li><li>Coffee Capsules</li>
        </ul>
        <div class="more">MORE ▸</div>
        <h3 class="side-title">Choose Coffee by Use</h3>
        <ul class="side-list">
          <li>For Moka Pots</li><li>For Espresso Machines</li><li>For Cafetieres</li><li>For Filter Machines</li><li>For Bean-to-Cup</li><li>Capsule Compatible</li>
        </ul>
        <div class="more">MORE ▸</div>
        <h3 class="side-title">Popular Brands</h3>
        <ul class="side-list">
          <li>Torrevalle Caffè</li><li>Mirando Roast</li><li>Casaluce</li><li>Pietrafina</li><li>Orvano</li>
        </ul>
      </aside>

      <main class="main">
        <div class="welcome">
          <h1>Welcome to <em>brewlantern!</em></h1>
          <h2>The place to buy espresso coffee online...</h2>
          <p>Enjoy drinking some of the best and most sought after coffee around, including roasts from small family houses across Italy and beyond. We stock a wide range of coffee beans and ground coffee, all carefully selected for their flavour and freshness.</p>
          <p>Whether you brew with a moka pot, an espresso machine or a cafetiere, you will find a blend to suit your taste. Orders placed before noon are dispatched the same day, and delivery is free on all orders over £60.</p>
          <p>For news, offers and brewing tips, visit our Chatterly page or sign up to our newsletter today.</p>
          <span class="read-more">Read More</span>
        </div>

        <div class="section-bar">
          <svg width="16" height="12" viewBox="0 0 16 12"><path d="M1 3h10v4a4 4 0 0 1-4 4H5a4 4 0 0 1-4-4z" fill="#fff"/><path d="M11 4h2a2 2 0 0 1 0 4h-2" stroke="#fff" fill="none" stroke-width="1.3"/></svg>
          HOT PRODUCTS
        </div>

        <div class="product-grid">
          <div class="product"><div class="product-img"></div><p class="product-name">Nullam in velit lorem</p><p class="product-price">Price: £0.00</p></div>
          <div class="product"><div class="product-img"></div><p class="product-name">Nullam in velit lorem</p><p class="product-price">Price: £0.00</p></div>
          <div class="product"><div class="product-img"></div><p class="product-name">Nullam in velit lorem</p><p class="product-price">Price: £0.00</p></div>
          <div class="product"><div class="product-img"></div><p class="product-name">Nullam in velit lorem</p><p class="product-price">Price: £0.00</p></div>
        </div>
      </main>
    </div>
  </div>
</div>
</body>
</html>
```